Security Officer Training Certifications POSTCARD

We need Post Card Design
-Front and Back
-In Compliance with BRAMBLE INK for upload!
-For Oversized and Jumbo Size Cards (bramble inks)

Our Company:
www.patrolcraftacademyhubzone.org (FOR IDEAS)

We provide Corporate Security Officer/Criminal Justice/Police Tactics Training for Private Companies that have a security department and officers.

We provide:
Handcuffing certifications
Pepper Spray
Compliance Training
Instructor Training
California Guard Card

FRONT DESIGN TO BE VERY CATCH!
Back of Card List of Services/Menu

Our Card to display powerful image for a Security Officer Department
Traits in Pic and Deigns
VALUE
COMPETITIVE EDGE
PROFESSIONAL GROWTH
QUALITY
PROFICIENT/EFFECTIVE SECURITY OFFICERS
TACTICAL OFFICERS
PROFESSIONALISM
EXPERTS
INDUSTRY LEADERS
READINESS

Target Market(s)

Proprietary Security Officer Department. Agencies that hire their own guard force.
It will be owners of security guard companies, Security Directors, manager

Industry/Entity Type

Security

Requirements
Must have
• GREAT FROM OF CARD PICTURE that encompasses
• Corporate Security Officers
• MUST HAVE A COOL LOOK!
• Professionalism
• Tactical
• The best
• Upgrade skills
• BACK of Card:
• Like list of services with pics and cool stuff
• PICS of Security Officer /Police Professionals
• with great backgrounds!
• COOL
• BACK OF CARD
• Space to have address of receipient
• space for post age
• in ACCORDANCE with BRAMBLE INKS to upload...

```html
<!DOCTYPE html>
<html lang="en">
<head>
<meta charset="utf-8">
<title>Security Corporate Training Postcard</title>
<link rel="stylesheet" href="https://fonts.googleapis.com/css2?family=Tinos:wght@400;700&family=Arimo:wght@400;700&display=swap">
<style>
:root{
  --stage:#8a8a8a;
  --blue:#2e3192;
  --blue-deep:#1c1f66;
  --blue-night:#15184f;
  --white:#ffffff;
  --yellow:#f4e04d;
  --ink:#333333;
  --rule:#9a9a9a;
}
*{margin:0;padding:0;box-sizing:border-box}
html,body{width:1200px;height:458px;overflow:hidden}
body{background:radial-gradient(ellipse at center,#a8a8a8 0%,var(--stage) 70%,#6e6e6e 100%);position:relative;font-family:"Arimo",Arial,sans-serif}
.card{position:absolute;top:54px;width:532px;height:344px;overflow:hidden;background:var(--white)}
.front{left:42px}
.back{left:623px;width:530px}
.front svg.art{position:absolute;inset:0}
.brand{position:absolute;left:306px;top:52px;width:116px;height:116px;border-radius:50%;background:var(--white);display:flex;align-items:center;justify-content:center;text-align:center;padding:16px;font-family:"Tinos",serif;font-weight:700;font-size:13px;line-height:1.2;color:var(--blue)}
.front-title{position:absolute;left:230px;width:280px;top:188px;text-align:center;font-family:"Tinos",serif;font-weight:700;font-size:21px;line-height:1.2;color:var(--white);letter-spacing:.3px}
.front-sub{position:absolute;left:200px;width:340px;top:248px;text-align:center;font-family:"Tinos",serif;font-size:14px;line-height:1.45;color:var(--white)}
.tagline{position:absolute;left:0;right:0;top:302px;height:42px;display:flex;justify-content:flex-end;align-items:center;gap:18px;padding-right:16px;font-family:"Tinos",serif;font-size:15px;color:var(--white)}
.tagline .sep{opacity:.9}
.menu{position:absolute;left:0;top:0;width:326px;height:344px;background:linear-gradient(160deg,#3438a0 0%,var(--blue) 55%,#282b85 100%)}
.menu-head{position:absolute;top:10px;left:0;right:0;text-align:center;font-family:"Tinos",serif;font-weight:700;font-size:12.5px;line-height:1.3;color:var(--white)}
.col-rule{position:absolute;left:164px;top:54px;width:1px;height:222px;background:rgba(255,255,255,.35)}
.row-rule{position:absolute;left:12px;width:302px;height:1px;background:rgba(255,255,255,.35)}
.service{position:absolute;width:150px;color:var(--white)}
.service h3{font-family:"Tinos",serif;font-weight:700;font-size:8.5px;line-height:1.2}
.service .price{font-family:"Tinos",serif;font-weight:700;font-size:5.6px;color:var(--yellow);margin:3px 0 4px}
.service ul{list-style:none}
.service li{font-size:4.6px;line-height:1.25;margin-bottom:5.2px;padding-left:7px;position:relative}
.service li::before{content:"✓";position:absolute;left:0;top:-.5px;font-size:5.2px}
.service li.strong{font-weight:700}
.site{position:absolute;left:174px;top:280px;font-family:"Tinos",serif;font-weight:700;font-size:7.6px;color:var(--white)}
.call-band{position:absolute;left:0;top:308px;width:326px;height:28px;background:var(--blue-night);display:flex;align-items:center;justify-content:center;font-family:"Tinos",serif;font-weight:700;font-size:13px;color:var(--white)}
.return-address{position:absolute;left:337px;top:20px;font-size:5.4px;line-height:1.55;color:var(--ink)}
.return-address p+p{margin-top:4px}
.stamp-box{position:absolute;left:470px;top:16px;width:47px;height:47px;border:1px solid var(--rule)}
.seal{position:absolute;left:289px;top:118px;width:80px;height:80px;border-radius:50%;background:var(--white);border:2px solid var(--blue);display:flex;align-items:center;justify-content:center;text-align:center;padding:10px;font-family:"Tinos",serif;font-weight:700;font-size:8px;line-height:1.2;color:var(--blue)}
.address-line{position:absolute;left:341px;width:171px;height:1px;background:var(--rule)}
</style>
</head>
<body>

<section class="card front" aria-label="Postcard front">
  <svg class="art" width="532" height="344" viewBox="0 0 532 344" aria-hidden="true">
    <defs>
      <linearGradient id="sky" x1="0" y1="0" x2="1" y2="1">
        <stop offset="0" stop-color="#9fc2e2"/><stop offset="1" stop-color="#d7e3ea"/>
      </linearGradient>
      <linearGradient id="uniform" x1="0" y1="0" x2="1" y2="1">
        <stop offset="0" stop-color="#2a2c33"/><stop offset="1" stop-color="#6b6f77"/>
      </linearGradient>
      <linearGradient id="agent" x1="0" y1="0" x2="0" y2="1">
        <stop offset="0" stop-color="#b5c6d3"/><stop offset="1" stop-color="#2a2d3a"/>
      </linearGradient>
    </defs>
    <rect width="532" height="344" fill="url(#sky)"/>
    <rect x="40" y="0" width="230" height="280" fill="url(#uniform)" opacity=".55"/>
    <polygon points="0,80 170,240 70,344 0,344" fill="url(#uniform)"/>
    <polygon points="430,0 532,0 532,210 430,80" fill="url(#agent)"/>
    <polygon points="0,344 0,340 180,236 330,140 430,80 532,210 532,344" fill="#2e3192"/>
    <line x1="0" y1="80" x2="176" y2="244" stroke="#fff" stroke-width="3"/>
    <line x1="66" y1="344" x2="330" y2="140" stroke="#fff" stroke-width="3"/>
    <line x1="430" y1="80" x2="532" y2="212" stroke="#fff" stroke-width="3"/>
    <rect x="0" y="302" width="532" height="42" fill="#1c1f66"/>
  </svg>
  <div role="img" aria-label="Photo of a security officer speaking into a radio in front of a construction crane" style="position:absolute;left:40px;top:0;width:230px;height:200px"></div>
  <div role="img" aria-label="Photo of uniformed security officers standing in line" style="position:absolute;left:0;top:100px;width:120px;height:200px"></div>
  <div role="img" aria-label="Photo of a security agent in sunglasses on the phone" style="position:absolute;left:430px;top:0;width:102px;height:200px"></div>
  <div class="brand">Ridgeline Guard Institute</div>
  <h1 class="front-title">SECURITY CORPORATE TRAINING</h1>
  <p class="front-sub">Security Guard Training in Los Angeles<br>California Guard Card Specialists</p>
  <div class="tagline">
    <span>Professionalism</span><span class="sep">|</span>
    <span>Tactical</span><span class="sep">|</span>
    <span>The Best</span><span class="sep">|</span>
    <span>Upgrade Skills</span>
  </div>
</section>

<section class="card back" aria-label="Postcard back">
  <div class="menu">
    <h2 class="menu-head">On-Site – We come to you – SAVE on Staff Training<br>with our compliance &amp; training Seminars</h2>
    <div class="col-rule"></div>
    <div class="row-rule" style="top:164px"></div>
    <div class="row-rule" style="top:264px"></div>

    <div class="service" style="left:14px;top:56px">
      <h3>Handcuffing Certifications</h3>
      <p class="price">$1000 for up to 20 personnel</p>
      <ul>
        <li>Nomenclature – Basic Stance – Patterns of Movement Cover and Contact Officer</li>
        <li>Practical Application – Standing – Kneeling – Prone Positions</li>
        <li>Pat Downs, Searches – Report Writing</li>
        <li class="strong">4 hour operator training</li>
        <li>Certificates of Completion Issued Same Day</li>
      </ul>
    </div>

    <div class="service" style="left:174px;top:56px">
      <h3>Chemical Agents (Pepper Spray)</h3>
      <p class="price">$1000 for up to 20 personnel</p>
      <ul>
        <li>Defense tool – Use of Force</li>
        <li>Spraying Techniques – Disengaging – Patterns of Movement</li>
        <li>Drawing Techniques – Deployment Considerations – Tactical Considerations</li>
        <li>Decontamination Procedures – Report Writing</li>
        <li class="strong">4 hour operator training</li>
        <li>Certificate of Completion issued Same Day</li>
      </ul>
    </div>

    <div class="service" style="left:14px;top:172px">
      <h3>Compliance Training</h3>
      <p class="price">$1650 for up to 20 personnel</p>
      <ul>
        <li>Prevent law suits with compliance and refresher training</li>
        <li>Use of Force</li>
        <li>Officer Safety – CA laws</li>
        <li>Striking Techniques – Defensive Techniques</li>
        <li class="strong">4 hour operator training</li>
      </ul>
    </div>

    <div class="service" style="left:174px;top:172px">
      <h3>Instructor Training</h3>
      <p class="price">$1650 for up to 20 personnel</p>
      <ul>
        <li>State of the Art simulator, hundreds of real life scenarios</li>
        <li>Room Entry Tactics, Movement as a Team</li>
        <li>Clearing hallways and rooms</li>
        <li>Tactical Considerations</li>
        <li>Use of Simulator Firearms – 6 hour operator training</li>
        <li>Certificate of Training issued at end of program</li>
      </ul>
    </div>

    <div class="service" style="left:14px;top:273px">
      <h3>California Guard Card Certification</h3>
      <p class="price">$1200 for up to 25 personnel</p>
    </div>

    <p class="site">www.patrolcraftacademyhubzone.org</p>
    <p class="call-band">Call us now at 555- 010-2468</p>
  </div>

  <address class="return-address" style="font-style:normal">
    <p>1250 Harbor Lane<br>Fairview, CA 90000</p>
    <p>(555) 010-2468</p>
    <p>info@patrolcraftacademyhubzone.org</p>
  </address>
  <div class="stamp-box" aria-label="Postage area"></div>
  <div class="seal">Ridgeline Guard Institute</div>
  <div class="address-line" style="top:244px"></div>
  <div class="address-line" style="top:270px"></div>
  <div class="address-line" style="top:295px"></div>
</section>

</body>
</html>
```